" Busco uma arte para capa de um livro que estou concluindo. Título do livro: "Entre marés e faróis. Um diário de viagens pelo litoral esquecido". "

```html
<!DOCTYPE html>
<html lang="pt">
<head>
<meta charset="utf-8">
<title>Entre marés e faróis — capa</title>
<link rel="stylesheet" href="https://fonts.googleapis.com/css2?family=Cormorant+Garamond:wght@500;600&family=Playfair+Display:wght@800&display=swap">
<style>
  :root {
    --page-bg: #e9e7ea;
    --peach-top: #f6d3c3;
    --peach-low: #efc3b4;
    --ink: #2a2940;
    --sun: #fbf3ec;
    --hill-rose: #d9a6ae;
    --hill-lilac: #b79cc4;
    --hill-violet: #8c74ab;
    --hill-plum: #5f4f80;
    --night: #2c2a3b;
    --paper: #f3e2bd;
    --gold: #e0b96f;
  }
  * { margin: 0; padding: 0; box-sizing: border-box; }
  html, body {
    width: 1200px; height: 1200px; overflow: hidden;
    background: var(--page-bg);
  }
  .canvas {
    width: 1200px; height: 1200px;
    display: flex; align-items: center; justify-content: center;
  }
  .cover {
    position: relative;
    width: 780px; height: 1100px;
    background: linear-gradient(180deg, var(--peach-top) 0%, var(--peach-low) 50%);
    overflow: hidden;
    box-shadow: 0 10px 30px rgba(40, 35, 60, 0.18);
  }
  .author {
    position: absolute; top: 74px; left: 0; right: 0;
    text-align: center;
    font-family: "Cormorant Garamond", serif;
    font-weight: 600; font-size: 26px;
    color: var(--ink);
    letter-spacing: 0.5px;
  }
  .title {
    position: absolute; top: 196px; left: 0; right: 0;
    text-align: center; color: var(--ink);
  }
  .title-lead {
    display: block;
    font-family: "Cormorant Garamond", serif;
    font-weight: 600; font-size: 58px; line-height: 1;
    transform: scaleX(0.85);
  }
  .title-main {
    display: block;
    font-family: "Playfair Display", serif;
    font-weight: 800; font-size: 118px; line-height: 1.05;
    transform: scaleX(0.82);
  }
  .subtitle {
    position: absolute; top: 392px; left: 0; right: 0;
    text-align: center;
    font-family: "Cormorant Garamond", serif;
    font-weight: 500; font-size: 38px; line-height: 1.1;
    color: var(--ink);
  }
  .landscape {
    position: absolute; left: 0; top: 0;
    width: 780px; height: 1100px;
  }
  .illustration {
    position: absolute;
    left: 90px; top: 600px;
    width: 620px; height: 420px;
    border-radius: 50% 50% 46% 46%;
    background:
      radial-gradient(ellipse 60% 45% at 58% 78%, var(--paper) 0%, var(--gold) 45%, rgba(224,185,111,0) 75%),
      radial-gradient(ellipse 70% 55% at 45% 40%, rgba(183,156,196,0.9) 0%, rgba(140,116,171,0.6) 55%, rgba(95,79,128,0) 100%);
  }
</style>
</head>
<body>
  <main class="canvas">
    <article class="cover">
      <svg class="landscape" viewBox="0 0 780 1100" aria-hidden="true">
        <circle cx="690" cy="270" r="22" fill="var(--sun)"/>
        <path d="M0 560 C120 520 220 540 330 575 C450 610 560 520 780 540 L780 1100 L0 1100 Z" fill="var(--hill-rose)"/>
        <path d="M0 620 C140 580 260 640 380 630 C520 615 620 570 780 600 L780 1100 L0 1100 Z" fill="var(--hill-lilac)"/>
        <path d="M0 700 C150 660 280 720 420 700 C560 680 660 650 780 690 L780 1100 L0 1100 Z" fill="var(--hill-violet)"/>
        <path d="M0 800 C160 770 300 820 450 800 C590 780 690 770 780 790 L780 1100 L0 1100 Z" fill="var(--hill-plum)"/>
        <path d="M0 900 C180 880 320 930 480 915 C620 900 710 890 780 900 L780 1100 L0 1100 Z" fill="var(--night)"/>
      </svg>
      <div class="illustration" role="img"
           aria-label="Ilustração central: livro aberto de onde saem penas, tinteiro, letras e flores, com pássaros voando sobre as colinas"></div>
      <p class="author">Helena Duarte Ramos</p>
      <h1 class="title">
        <span class="title-lead">Entre marés e</span>
        <span class="title-main">faróis</span>
      </h1>
      <p class="subtitle">Um diário de viagens pelo<br>litoral esquecido</p>
    </article>
  </main>
</body>
</html>
```